bright meridian advisory needs a business card

i need a business card with a logo that will also be used on the website. The company name is "Bright Meridian Advisory"
The business is an advisory and training organisation that specialises in finding a companys 'natural sequence' to success but we will also provide mentoring and counselling to individuals that want to unlock their potential. The process is unique and not full of the normal corporate bullshit so the card should be 'different' and innovative in use of texture, colour, layout etc...I have no guiding principles for you but if you were the head of a new company lloking to make a great first impression what would your card look like? It should have enough of the corporate that the stiffs dont get scared but should be cool enough that the cool kids get it :-)

Target Market(s)

Companies and people looking to grow their staff capabilities. Specialising in IT but can transcend that to other lines of business.

Industry/Entity Type

It Company

Contact Information for Business Card

usuall placeholder stuff Name, Number etc

Requirements
Must have
• cool and innovative logo and use of space
Nice to have
• Background image, subtle use of the caffeine molecule
• A rollable business card similar to the attached image. Would be nice if either side of the card could be half of a DNA helix and by rolling 2 sides together they could connect at one or more points....Perhaps the strands between have a message?
Should not have
• boring usual business card look and feel

```html
<!DOCTYPE html>
<html lang="en">
<head>
<meta charset="utf-8">
<title>Bright Meridian Advisory – Business Card</title>
<link rel="stylesheet" href="https://fonts.googleapis.com/css2?family=Cinzel:wght@400;600&display=swap">
<style>
  :root {
    --page: #ffffff;
    --brand-blue: #0b6fb4;
    --panel-blue: #0a6fb5;
    --tint-blue: #d8ebf8;
    --soft-blue: #4fa3dc;
    --helix-light: #8fc4ea;
    --text-grey: #5a5a5a;
    --edge: #6b7a86;
  }
  * { margin: 0; padding: 0; box-sizing: border-box; }
  html, body { width: 1200px; height: 846px; overflow: hidden; background: var(--page); }
  body { position: relative; font-family: "Cinzel", serif; }

  .card {
    position: absolute;
    top: 204px;
    width: 466px;
    height: 260px;
    border: 1px solid var(--edge);
    box-shadow: 6px 8px 10px rgba(0,0,0,0.28);
    overflow: hidden;
  }
  .card--front { left: 128px; background: var(--page); }
  .card--back { left: 616px; background: var(--panel-blue); }

  .card__tint { position: absolute; inset: 0; }

  .card__panel {
    position: absolute;
    top: 0; right: 0;
    width: 135px; height: 100%;
    background: var(--panel-blue);
  }

  .helix {
    position: absolute;
    border-radius: 40px;
    background: linear-gradient(160deg, rgba(143,196,234,0.55), rgba(79,163,220,0.35));
  }
  .helix--front { top: 18px; right: 6px; width: 112px; height: 120px; transform: skewX(-18deg); }
  .helix--back { top: 80px; left: -20px; width: 150px; height: 150px; transform: skewX(-18deg); }

  .brand-name {
    position: absolute;
    top: 24px; left: 30px;
    font-size: 14px;
    font-weight: 600;
    letter-spacing: 0.5px;
    color: var(--brand-blue);
  }

  .person {
    position: absolute;
    top: 100px; right: 145px;
    text-align: right;
  }
  .person__name { font-size: 15px; font-weight: 600; color: var(--brand-blue); letter-spacing: 0.5px; }
  .person__title { font-size: 10.5px; color: var(--text-grey); margin-top: 2px; letter-spacing: 0.5px; }

  .name-tab { position: absolute; top: 104px; left: 331px; }

  .contact {
    position: absolute;
    top: 183px; right: 145px;
    list-style: none;
    text-align: right;
    font-size: 9.5px;
    line-height: 13.5px;
    color: var(--text-grey);
    letter-spacing: 0.4px;
  }
  .contact-icons {
    position: absolute;
    top: 185px; left: 338px;
    display: flex; flex-direction: column; gap: 4px;
  }

  .back-name {
    position: absolute;
    top: 110px; left: 0; width: 100%;
    padding-left: 110px;
    text-align: center;
    font-size: 17px;
    font-weight: 600;
    letter-spacing: 1px;
    color: var(--soft-blue);
  }

  .main-logo {
    position: absolute;
    top: 748px; left: 0; width: 100%;
    text-align: center;
    font-size: 26px;
    font-weight: 600;
    letter-spacing: 1.5px;
    color: var(--brand-blue);
  }
</style>
</head>
<body>

  <section class="card card--front" aria-label="Business card front">
    <svg class="card__tint" width="466" height="260" viewBox="0 0 466 260" aria-hidden="true">
      <polygon points="277,0 331,0 331,260 0,260" fill="var(--tint-blue)"/>
    </svg>
    <div class="card__panel"></div>
    <div class="helix helix--front" role="img" aria-label="Illustrated DNA helix strand"></div>

    <div class="brand-name">Bright Meridian Advisory</div>

    <svg class="name-tab" width="8" height="14" viewBox="0 0 8 14" aria-hidden="true">
      <polygon points="0,0 8,7 0,14" fill="var(--tint-blue)"/>
    </svg>
    <div class="person">
      <div class="person__name">Persons Name</div>
      <div class="person__title">Persons Title</div>
    </div>

    <ul class="contact">
      <li>0400 512 208</li>
      <li>0400 619 374</li>
      <li>brightmeridianadvisory.com</li>
      <li>hello@brightmeridianadvisory.com</li>
    </ul>

    <div class="contact-icons" aria-hidden="true">
      <svg width="9" height="9" viewBox="0 0 10 10"><path d="M2 1l2 2-1 1.5c.7 1.3 1.4 2 2.5 2.5L7 6l2 2-1.5 1.5C4.5 9 1 5.5.5 2.5z" fill="var(--helix-light)"/></svg>
      <svg width="9" height="9" viewBox="0 0 10 10"><path d="M5 0a3.5 3.5 0 0 1 3.5 3.5C8.5 6 5 10 5 10S1.5 6 1.5 3.5A3.5 3.5 0 0 1 5 0z" fill="var(--helix-light)"/></svg>
      <svg width="9" height="9" viewBox="0 0 10 10"><circle cx="5" cy="5" r="4.5" fill="var(--helix-light)"/></svg>
      <svg width="9" height="9" viewBox="0 0 10 10"><rect x="0.5" y="2" width="9" height="6.5" fill="var(--helix-light)"/></svg>
    </div>
  </section>

  <section class="card card--back" aria-label="Business card back">
    <div class="helix helix--back" role="img" aria-label="Illustrated DNA helix strand continuing from the front"></div>
    <div class="back-name">Bright Meridian Advisory</div>
  </section>

  <div class="main-logo">Bright Meridian Advisory</div>

</body>
</html>
```